New Label Design Project for Tinkers den wines

I would like to purchase a customized version of a design you have previously submitted - https://www.artmarketfolio.com.au/design/57302946

We need a label that that we can use for our new vintage shiraz, Merlot and Pinot Noir products. This Label will be just 1 label that will be front and back label.
Please see attached

Target Market(s)

young and old wine drinkers

Industry/Entity Type

Wine

Colors

Designer to choose colors to be used in the design.

Requirements
Must have
• logo but also is a bit funky
Nice to have
• mixture of Funky and Modern

```html
<!DOCTYPE html>
<html lang="en">
<head>
<meta charset="utf-8">
<title>Tinker's Den – Label Set</title>
<link rel="stylesheet" href="https://fonts.googleapis.com/css2?family=Cinzel:wght@400;600&family=EB+Garamond:wght@400&display=swap">
<style>
  :root {
    --paper: #ffffff;
    --label-black: #050505;
    --wine-red: #a41c22;
    --band-red: #b51f27;
    --gold-light: #e8cfa3;
    --gold-dark: #a98a5c;
    --gold-text: #c9a45c;
    --text-light: #e9e9e9;
    --text-muted: #bdbdbd;
    --barrel-dark: #1c1c1c;
    --barrel-mid: #3a3a3a;
  }
  * { margin: 0; padding: 0; box-sizing: border-box; }
  html, body { width: 800px; height: 1200px; overflow: hidden; background: var(--paper); }
  .canvas { position: relative; width: 800px; height: 1200px; }

  .label-set { position: absolute; top: 334px; width: 360px; height: 520px; }
  .label-set--shiraz { left: 20px; }
  .label-set--pinot { left: 459px; }

  /* Neck strip */
  .neck-strip {
    position: absolute; left: 0; top: 0; width: 43px; height: 421px;
    background: var(--label-black); border-radius: 22px;
  }
  .neck-strip__name {
    position: absolute; left: 50%; width: 130px; margin-left: -65px;
    font-family: "Cinzel", serif; font-weight: 400; font-size: 10px;
    letter-spacing: 0.08em; color: var(--gold-text); text-align: center;
    transform: rotate(90deg);
  }
  .neck-strip__name--top { top: 80px; }
  .neck-strip__name--bottom { top: 330px; transform: rotate(-90deg); }
  .neck-strip__dot {
    position: absolute; left: 15px; top: 200px; width: 13px; height: 13px;
    border: 1px solid var(--gold-text); border-radius: 50%;
  }

  /* Front label */
  .front-label {
    position: absolute; left: 68px; top: 4px; width: 259px; height: 334px;
    background: var(--label-black); color: var(--text-light);
  }
  .front-label__banner { position: absolute; left: 55px; top: 0; width: 148px; height: 157px; }
  .front-label__brand {
    position: absolute; left: 55px; top: 76px; width: 148px; text-align: center;
    font-family: "Cinzel", serif; font-weight: 600; font-size: 21px; line-height: 1.15;
    color: #ffffff; letter-spacing: 0.03em;
  }
  .front-label__variety {
    position: absolute; left: 0; top: 180px; width: 100%; text-align: center;
    font-family: "Cinzel", serif; font-size: 13px; letter-spacing: 0.2em;
  }
  .front-label__region {
    position: absolute; left: 0; top: 198px; width: 100%; text-align: center;
    font-family: "Cinzel", serif; font-size: 10px; letter-spacing: 0.2em; color: var(--text-muted);
  }
  .front-label__barrels {
    position: absolute; left: 50px; top: 220px; width: 160px; height: 58px;
    border-radius: 24px 24px 6px 6px;
    background: linear-gradient(180deg, var(--barrel-mid), var(--barrel-dark));
  }
  .front-label__band {
    position: absolute; left: 0; top: 279px; width: 100%; height: 14px;
    text-align: center; font-family: "Cinzel", serif; font-size: 10.5px; line-height: 14px;
    letter-spacing: 0.12em; color: #1a1a1a;
  }
  .front-label__band--gold {
    background: linear-gradient(90deg, var(--gold-dark), var(--gold-light) 30%, var(--gold-light) 70%, var(--gold-dark));
  }
  .front-label__band--red { background: var(--band-red); color: #ffffff; }
  .front-label__vintage {
    position: absolute; left: 0; top: 316px; width: 100%; text-align: center;
    font-family: "EB Garamond", serif; font-size: 9px;
  }
  .front-label__volume {
    position: absolute; right: 16px; top: 313px;
    font-family: "EB Garamond", serif; font-size: 10px;
  }

  /* Back label */
  .back-label {
    position: absolute; left: 91px; top: 348px; width: 212px; height: 174px;
    background: var(--label-black); color: var(--text-light);
    font-family: "EB Garamond", serif;
  }
  .back-label__brand {
    position: absolute; left: 0; top: 36px; width: 100%; text-align: center;
    font-family: "Cinzel", serif; font-weight: 600; font-size: 15px; color: var(--wine-red);
    letter-spacing: 0.04em;
  }
  .back-label__title {
    position: absolute; left: 0; top: 62px; width: 100%; text-align: center;
    font-size: 9.5px; letter-spacing: 0.1em; line-height: 1.35; text-transform: uppercase;
  }
  .back-label__notes {
    position: absolute; left: 0; top: 90px; width: 100%; text-align: center;
    font-size: 7.5px; line-height: 1.45; color: var(--text-muted);
  }
  .back-label__origin {
    position: absolute; left: 10px; top: 115px; font-size: 8px; letter-spacing: 0.06em;
  }
  .back-label__legal {
    position: absolute; left: 10px; top: 128px; font-family: Arial, sans-serif;
    font-size: 5px; line-height: 1.55; color: var(--text-light);
  }
  .back-label__blank {
    position: absolute; right: 9px; top: 113px; width: 76px; height: 56px; background: #ffffff;
  }
</style>
</head>
<body>
<main class="canvas">

  <!-- Shiraz set -->
  <section class="label-set label-set--shiraz">
    <div class="neck-strip">
      <span class="neck-strip__name neck-strip__name--top">Tinker's Den</span>
      <span class="neck-strip__dot"></span>
      <span class="neck-strip__name neck-strip__name--bottom">Tinker's Den</span>
    </div>

    <div class="front-label">
      <svg class="front-label__banner" viewBox="0 0 148 157" aria-hidden="true">
        <polygon points="0,0 148,0 148,122 74,157 0,122" fill="var(--wine-red)"/>
      </svg>
      <div class="front-label__brand">Tinker's<br>Den</div>
      <div class="front-label__variety">SHIRAZ</div>
      <div class="front-label__region">Mt. Benson</div>
      <div class="front-label__barrels" role="img" aria-label="Stacked oak wine barrels illustration"></div>
      <div class="front-label__band front-label__band--gold">WINE OF AUSTRALIA</div>
      <div class="front-label__vintage">2017</div>
      <div class="front-label__volume">750mL</div>
    </div>

    <div class="back-label">
      <div class="back-label__brand">Tinker's Den</div>
      <div class="back-label__title">2007 Shiraz Mt. Benson<br>South Australia</div>
      <div class="back-label__notes">This mature, smooth Shiraz matches most savoury foods<br>and any occasion. Drink now and enjoy.</div>
      <div class="back-label__origin">WINE OF AUSTRALIA</div>
      <div class="back-label__legal">OAKVALE TRADING PTY LTD<br>Redhill Victoria 3100 Australia<br>13.6% ALC/VOL<br>APPROX. 8.0 STANDARD DRINKS<br>Preservative 220 added.</div>
      <div class="back-label__blank"></div>
    </div>
  </section>

  <!-- Pinot Noir set -->
  <section class="label-set label-set--pinot">
    <div class="neck-strip">
      <span class="neck-strip__name neck-strip__name--top">Tinker's Den</span>
      <span class="neck-strip__dot"></span>
      <span class="neck-strip__name neck-strip__name--bottom">Tinker's Den</span>
    </div>

    <div class="front-label">
      <svg class="front-label__banner" viewBox="0 0 148 157" aria-hidden="true">
        <polygon points="0,0 148,0 148,122 74,157 0,122" fill="var(--wine-red)"/>
      </svg>
      <div class="front-label__brand">Tinker's<br>Den</div>
      <div class="front-label__variety">PINOT NOIR</div>
      <div class="front-label__barrels" role="img" aria-label="Stacked oak wine barrels illustration"></div>
      <div class="front-label__band front-label__band--red">WINE OF AUSTRALIA</div>
      <div class="front-label__vintage">2017</div>
      <div class="front-label__volume">750mL</div>
    </div>

    <div class="back-label">
      <div class="back-label__brand">Tinker's Den</div>
      <div class="back-label__title">2007 Shiraz Mt. Benson<br>South Australia</div>
      <div class="back-label__notes">This mature, smooth Shiraz matches most savoury foods<br>and any occasion. Drink now and enjoy.</div>
      <div class="back-label__origin">WINE OF AUSTRALIA</div>
      <div class="back-label__legal">OAKVALE TRADING PTY LTD<br>Redhill Victoria 3100 Australia<br>13.6% ALC/VOL<br>APPROX. 8.0 STANDARD DRINKS<br>Preservative 220 added.</div>
      <div class="back-label__blank"></div>
    </div>
  </section>

</main>
</body>
</html>
```